Business Card for a mobile physiotherapy company

I need a layout for a business card for a mobile physiotherapy company.
Slogan is "Mobile Physiotherapy - Your Road To Recovery"
Phone number is 867-402-5913
Email VantrePhysio@mailbright.ca (subject to change with website)
Website www.VantrePhysio.ca
My name and credentials: Kent Vantre Kent Vantre, BSc(kin), MPT, CAFCI, IMS
Information maybe included: Direct Billing, Services including Physiotherapy, IMS, acupuncture
Maybe include facebook and instagram logos
One side with the logo clean and sharp
Other side with details, try not to look too busy, keep everything concise

```html
<!DOCTYPE html>
<html lang="en">
<head>
<meta charset="utf-8">
<title>Vantre Physio – Business Card</title>
<link rel="stylesheet" href="https://fonts.googleapis.com/css2?family=Archivo:wght@800&family=Arimo:wght@400;700&display=swap">
<style>
  :root {
    --navy: #2a4a78;
    --forest: #0f574a;
    --paper: #ffffff;
    --backdrop: #e6e7e9;
  }
  * { box-sizing: border-box; margin: 0; padding: 0; }
  html, body { width: 1200px; height: 815px; overflow: hidden; }
  body {
    background: var(--backdrop);
    font-family: "Arimo", Arial, sans-serif;
    display: flex;
    flex-direction: column;
    align-items: center;
    justify-content: center;
    gap: 30px;
  }
  .card {
    position: relative;
    width: 640px;
    height: 366px;
    overflow: hidden;
    box-shadow: 0 6px 18px rgba(0,0,0,0.18);
  }

  /* Logo side */
  .card--logo {
    background: var(--navy);
    display: flex;
    align-items: center;
    justify-content: center;
  }
  .wordmark {
    display: flex;
    flex-direction: column;
    align-items: center;
    font-weight: 700;
    line-height: 1;
  }
  .wordmark__name { font-size: 68px; letter-spacing: 8px; }
  .wordmark__tag { font-size: 26px; letter-spacing: 19px; margin-top: 12px; padding-left: 19px; }
  .card--logo .wordmark { color: var(--paper); }

  /* Details side */
  .card--details { background: var(--paper); }
  .band-left {
    position: absolute; left: 0; top: 0; bottom: 0; width: 30px;
    background: var(--navy);
  }
  .band-left__accent {
    position: absolute; left: 10px; top: 50px; width: 26px; height: 58px;
    background: var(--forest);
    border-top: 4px solid var(--paper);
    border-bottom: 4px solid var(--paper);
  }
  .band-right {
    position: absolute; right: 10px; top: 0; bottom: 0; width: 13px;
    background: var(--forest);
  }
  .identity { position: absolute; left: 64px; top: 52px; }
  .identity__name {
    font-family: "Archivo", "Arial Black", sans-serif;
    font-weight: 800;
    font-size: 33px;
    letter-spacing: 1px;
    color: var(--forest);
    line-height: 1;
    padding-bottom: 4px;
    border-bottom: 2px solid var(--navy);
    display: inline-block;
  }
  .identity__credentials {
    font-size: 12.5px;
    letter-spacing: 0.6px;
    color: var(--forest);
    margin-top: 5px;
  }
  .contact {
    position: absolute; left: 52px; top: 232px;
    list-style: none;
    color: var(--forest);
    font-size: 15.5px;
    letter-spacing: 0.8px;
  }
  .contact__item { display: flex; align-items: center; gap: 12px; height: 24px; }
  .contact__icon { width: 15px; height: 15px; fill: var(--forest); flex: none; }
  .card--details .wordmark {
    position: absolute; right: 48px; top: 118px;
    color: var(--navy);
  }
  .card--details .wordmark__name { font-size: 52px; letter-spacing: 6px; }
  .card--details .wordmark__tag { font-size: 20px; letter-spacing: 15px; margin-top: 10px; padding-left: 15px; }
  .social {
    position: absolute; left: 452px; top: 296px;
    display: flex; gap: 7px;
  }
  .social__tile { width: 26px; height: 26px; border-radius: 5px; background: var(--navy); }
  .social__tile--alt { background: var(--forest); }
</style>
</head>
<body>
  <section class="card card--logo" aria-label="Card logo side">
    <div class="wordmark">
      <span class="wordmark__name">VANTRE</span>
      <span class="wordmark__tag">PHYSIO</span>
    </div>
  </section>

  <section class="card card--details" aria-label="Card details side">
    <div class="band-left"></div>
    <div class="band-left__accent"></div>
    <div class="band-right"></div>

    <div class="identity">
      <h1 class="identity__name">KENT VANTRE</h1>
      <p class="identity__credentials">Kent Vantre, BSc(kin), MPT, CAFCI, IMS</p>
    </div>

    <div class="wordmark">
      <span class="wordmark__name">VANTRE</span>
      <span class="wordmark__tag">PHYSIO</span>
    </div>

    <ul class="contact">
      <li class="contact__item">
        <svg class="contact__icon" viewBox="0 0 24 24" aria-hidden="true"><path d="M6.6 10.8a15 15 0 0 0 6.6 6.6l2.2-2.2c.3-.3.7-.4 1-.2 1.1.4 2.3.6 3.6.6.6 0 1 .4 1 1V20c0 .6-.4 1-1 1A17 17 0 0 1 3 4c0-.6.4-1 1-1h3.5c.6 0 1 .4 1 1 0 1.3.2 2.5.6 3.6.1.3 0 .7-.2 1z"/></svg>
        <span>867-402-5913</span>
      </li>
      <li class="contact__item">
        <svg class="contact__icon" viewBox="0 0 24 24" aria-hidden="true"><path d="M2 5h20v2l-10 6L2 7zm0 4.3 10 6 10-6V19H2z"/></svg>
        <span>VantrePhysio@mailbright.ca</span>
      </li>
      <li class="contact__item">
        <svg class="contact__icon" viewBox="0 0 24 24" aria-hidden="true"><path d="M12 2a10 10 0 1 0 0 20 10 10 0 0 0 0-20zm7.9 9h-3.4a15 15 0 0 0-1.3-6.2A8 8 0 0 1 19.9 11zM12 4.1c1 1.3 2.3 3.7 2.5 6.9h-5C9.7 7.8 11 5.4 12 4.1zM8.8 4.8A15 15 0 0 0 7.5 11H4.1a8 8 0 0 1 4.7-6.2zM4.1 13h3.4a15 15 0 0 0 1.3 6.2A8 8 0 0 1 4.1 13zm7.9 6.9c-1-1.3-2.3-3.7-2.5-6.9h5c-.2 3.2-1.5 5.6-2.5 6.9zm3.2-.7a15 15 0 0 0 1.3-6.2h3.4a8 8 0 0 1-4.7 6.2z"/></svg>
        <span>www.VantrePhysio.ca</span>
      </li>
    </ul>

    <div class="social" aria-hidden="true">
      <span class="social__tile"></span>
      <span class="social__tile social__tile--alt"></span>
    </div>
  </section>
</body>
</html>
```